Vinyl Apple Design of House Music Label

We need an apple vinyl record design of both sides (a round sticker in the middle of the vinyl record). We write minimal and house music. Like Tom Vesk and Morris Quade. We would like to see the design in bright colors, with patterns and swirls. Also, for future releases, the design of each release will change slightly. Easily changeable designs - welcome. Sizes attached.

Requirements
Nice to have
• Everything is at the discretion of the designer, but here are some of the works that I liked-
• https://www.platteneck.example/Morris_Quade_Folded_BRINE026_Vinyl__512840
• https://www.platteneck.example/Morris_Quade_Copper_Drift_EP_LOOM032_Vinyl__627194
• https://www.platteneck.example/Morris_Quade_%26_Gideon_Pratt_Vtrx_Ep_BRINE021_Vinyl__735402
• https://www.platteneck.example/Pulo_Varsk_Amber_Deck_Whorl_EP_TLVS004_Vinyl__518093
• https://www.platteneck.example/Dominic_Fairway_Ninth_Lattice_Ep_WXP006_Vinyl__604271
• https://www.platteneck.example/Moss_Harbor_Quiet_EP_KLV001_Vinyl__381657
• https://www.platteneck.example/Fenzo_Wolkenbruch_GAD006_Vinyl__274519
• https://www.platteneck.example/Lev_Tarko_Hollow_Signals_WN12_Vinyl__815364
• https://www.platteneck.example/Drisa_Tilt_Seven_EP_WN15_Vinyl__269487
• The content of the text is allowed, but not required. - label name (Velintor Records), 4 tracks (author and title), name of the distributor

```html
<!DOCTYPE html>
<html lang="en">
<head>
<meta charset="utf-8">
<title>Velintor Records – Vinyl Label, Side A and Side B</title>
<link rel="stylesheet" href="https://fonts.googleapis.com/css2?family=Pathway+Gothic+One&display=swap">
<style>
  :root {
    --bg: #ffffff;
    --blush: #ffa3a8;
    --coral: #e83030;
    --brick: #cc2a2e;
    --crimson: #b51619;
    --oxblood: #a80005;
    --tangerine: #e8770a;
    --cream: #ffe594;
    --rose: #e85f5f;
    --scarlet: #d90a0a;
    --signal: #ff0d0d;
    --garnet: #c0000a;
    --vermilion: #e54b0a;
    --apricot: #ffa452;
    --ink-orange: #e8690a;
    --spindle: #ffffff;
  }
  html, body {
    margin: 0;
    padding: 0;
    width: 1200px;
    height: 808px;
    overflow: hidden;
    background: var(--bg);
  }
  .canvas {
    display: block;
    width: 1200px;
    height: 808px;
  }
  .label-text {
    font-family: "Pathway Gothic One", "Arial Narrow", sans-serif;
    fill: var(--ink-orange);
  }
  .label-name { font-size: 33px; letter-spacing: 1px; }
  .track { font-size: 18px; }
  .cream-half { fill: var(--cream); }
  .rim { fill: none; stroke: var(--oxblood); stroke-width: 10; }
  .pointer { fill: var(--oxblood); }
  .spindle-hole { fill: var(--spindle); }
  .sw-blush { fill: var(--blush); }
  .sw-coral { fill: var(--coral); }
  .sw-brick { fill: var(--brick); }
  .sw-crimson { fill: var(--crimson); }
  .sw-oxblood { fill: var(--oxblood); }
  .sw-tangerine { fill: var(--tangerine); }
  .sw-cream { fill: var(--cream); }
  .sw-rose { fill: var(--rose); }
  .sw-scarlet { fill: var(--scarlet); }
  .sw-signal { fill: var(--signal); }
  .sw-garnet { fill: var(--garnet); }
  .sw-vermilion { fill: var(--vermilion); }
  .sw-apricot { fill: var(--apricot); }
</style>
</head>
<body>
<svg class="canvas" viewBox="0 0 1200 808" xmlns="http://www.w3.org/2000/svg">
  <defs>
    <radialGradient id="facet-tones" cx="0.5" cy="0.5" r="0.5">
      <stop offset="0" style="stop-color: var(--oxblood)"/>
      <stop offset="0.35" style="stop-color: var(--scarlet)"/>
      <stop offset="0.65" style="stop-color: var(--signal)"/>
      <stop offset="0.85" style="stop-color: var(--coral)"/>
      <stop offset="1" style="stop-color: var(--tangerine)"/>
    </radialGradient>
  </defs>

  <!-- Side A: label with track listing -->
  <g class="side side-a">
    <path role="img" aria-label="Low-poly pattern of red, orange, pink and cream triangles"
          d="M300 119 A266 266 0 0 0 300 651 Z" fill="url(#facet-tones)"/>
    <path class="cream-half" d="M300 119 A266 266 0 0 1 300 651 Z"/>
    <path class="rim" d="M300 124 A261 261 0 0 1 300 646"/>

    <text class="label-text label-name" x="311" y="242">VELINTOR</text>
    <text class="label-text label-name" x="311" y="271">RECORDS</text>

    <polygon class="pointer" points="312.5,322.5 327.5,317.5 335,331 312.5,352.5"/>
    <polygon class="pointer" points="327.5,365 365,355 370,372.5 335,375"/>
    <polygon class="pointer" points="327.5,397.5 365,397.5 367.5,416 337.5,412.5"/>
    <polygon class="pointer" points="312.5,420 335,437.5 330,452.5 312.5,457.5"/>

    <text class="label-text track" x="344" y="334">AUTHOR AND TITLE</text>
    <text class="label-text track" x="378" y="367">AUTHOR AND TITLE</text>
    <text class="label-text track" x="378" y="413">AUTHOR AND TITLE</text>
    <text class="label-text track" x="344" y="451">AUTHOR AND TITLE</text>

    <circle class="spindle-hole" cx="300" cy="385" r="15"/>
  </g>

  <!-- Side B: full pattern -->
  <g class="side side-b">
    <circle role="img" aria-label="Low-poly pattern of red, orange, pink and cream triangles"
            cx="890" cy="385" r="266" fill="url(#facet-tones)"/>
    <circle class="spindle-hole" cx="890" cy="385" r="15"/>
  </g>

  <!-- Colour palette -->
  <g class="palette">
    <rect class="sw-blush" x="59" y="693" width="32" height="30"/>
    <rect class="sw-coral" x="110" y="693" width="32" height="30"/>
    <rect class="sw-brick" x="161" y="693" width="32" height="30"/>
    <rect class="sw-crimson" x="212" y="693" width="32" height="30"/>
    <rect class="sw-oxblood" x="264" y="693" width="32" height="30"/>
    <rect class="sw-tangerine" x="316" y="693" width="32" height="30"/>
    <rect class="sw-cream" x="367" y="693" width="32" height="30"/>

    <rect class="sw-rose" x="59" y="743" width="32" height="30"/>
    <rect class="sw-scarlet" x="110" y="743" width="32" height="30"/>
    <rect class="sw-signal" x="161" y="743" width="32" height="30"/>
    <rect class="sw-garnet" x="212" y="743" width="32" height="30"/>
    <rect class="sw-vermilion" x="264" y="743" width="32" height="30"/>
    <rect class="sw-apricot" x="316" y="743" width="32" height="30"/>
  </g>
</svg>
</body>
</html>
```